Marlowe Consulting Cover 2 - Bright Ledger

Marlowe Consulting is a business consulting firm. We will publish a series of four thought leadership pieces online and via PDF. The second of the series is attached to this project. We need an eye-catching cover page with a back page that keeps with our branding. The document attached is in the final draft, and the cover and pack pages are placeholders only. You can find more about our branding and style on our website www.marloweconsulting.com.au. The other three projects can be found here with a similar brief, and you are welcome to submit a design for all 4.

```html
<!DOCTYPE html>
<html lang="en">
<head>
<meta charset="utf-8">
<title>Marlowe Consulting – Bright Ledger cover and back page</title>
<link rel="stylesheet" href="https://fonts.googleapis.com/css2?family=Poppins:wght@300;400;500;600;800&display=swap">
<style>
  :root {
    --bg: #f4f5f7;
    --ink-white: #ffffff;
    --brand-blue: #29a8e0;
    --brand-orange: #f7941d;
    --night: #0b0e14;
    --charcoal: #2b2e35;
    --sky-light: #e9eef5;
    --sky-mid: #a9bbd0;
    --glass-blue: #4a6890;
  }
  * { box-sizing: border-box; margin: 0; padding: 0; }
  html, body { width: 1200px; height: 1200px; overflow: hidden; }
  body {
    background: var(--bg);
    font-family: "Poppins", sans-serif;
    color: var(--ink-white);
    position: relative;
  }
  .page {
    position: absolute;
    top: 232px;
    width: 520px;
    height: 735px;
    overflow: hidden;
    background: var(--night);
    box-shadow: 0 18px 40px rgba(0,0,0,0.25);
  }
  .page--cover { left: 60px; }
  .page--back { left: 620px; }
  .page__photo {
    position: absolute; inset: 0;
    background: linear-gradient(170deg, var(--sky-light) 0%, var(--sky-mid) 40%, var(--glass-blue) 70%, #1b2638 100%);
  }
  .page__waves { position: absolute; inset: 0; width: 100%; height: 100%; }
  .brand {
    position: absolute; top: 40px; left: 36px;
    display: flex; align-items: center; gap: 10px;
  }
  .brand__dot {
    width: 34px; height: 34px; border-radius: 50%;
    background: var(--brand-orange);
  }
  .brand__name {
    font-weight: 600; font-size: 20px; line-height: 1.05;
    color: var(--brand-blue);
  }
  .cover__title {
    position: absolute; left: 36px; top: 468px; width: 470px;
    font-weight: 800; font-size: 31px; line-height: 1.25;
  }
  .cover__subtitle {
    position: absolute; left: 36px; top: 612px;
    font-weight: 400; font-size: 14px;
  }
  .band {
    position: absolute; left: 0; right: 0; top: 652px; height: 46px;
    background: var(--brand-blue);
    display: flex; align-items: center; justify-content: space-between;
    padding: 0 30px;
    font-weight: 300; font-size: 15px;
  }
  .band--cover { justify-content: flex-end; }
  .follow { display: flex; align-items: center; gap: 10px; font-size: 13px; }
  .follow__icon { width: 14px; height: 14px; border-radius: 50%; background: var(--ink-white); }
  .back__lead {
    position: absolute; left: 36px; top: 478px; width: 450px;
    font-weight: 500; font-size: 15px; line-height: 1.4;
  }
  .contacts {
    position: absolute; left: 36px; top: 540px; right: 20px;
    display: flex; gap: 28px;
  }
  .contact { font-size: 11px; line-height: 1.55; font-weight: 400; }
  .contact__name { font-weight: 600; font-size: 12px; }
  .contact__row { display: flex; align-items: center; gap: 6px; }
  .contact__icon { width: 12px; height: 12px; flex: none; }
</style>
</head>
<body>

<section class="page page--cover">
  <div class="page__photo" role="img" aria-label="Photograph placeholder: upward view of glass office towers against a bright sky"></div>
  <svg class="page__waves" viewBox="0 0 520 735" aria-hidden="true">
    <defs>
      <linearGradient id="coverDark" x1="0" y1="0" x2="0" y2="1">
        <stop offset="0" stop-color="#2b2e35" stop-opacity="0.95"/>
        <stop offset="1" stop-color="#0b0e14"/>
      </linearGradient>
    </defs>
    <path d="M0 405 C120 370 230 420 300 455 C350 478 375 460 368 400 C360 330 350 250 420 225 C460 210 500 210 520 200 L520 735 L0 735 Z" fill="url(#coverDark)"/>
    <path d="M0 388 C130 360 240 410 310 440 C345 455 360 440 355 395" fill="none" stroke="var(--brand-blue)" stroke-width="2"/>
    <path d="M0 405 C120 370 230 420 300 455 C350 478 375 460 368 400 C360 330 350 250 420 225 C460 210 500 210 520 200" fill="none" stroke="#fff" stroke-width="3"/>
    <rect x="0" y="698" width="520" height="37" fill="var(--night)"/>
  </svg>
  <div class="brand"><span class="brand__dot"></span><span class="brand__name">Marlowe<br>Consulting</span></div>
  <h1 class="cover__title">Bright Ledger:<br>Partnering with funds to<br>scale your business.</h1>
  <p class="cover__subtitle">Bridging valuation gaps in fund raising</p>
  <div class="band band--cover">marloweconsulting.com.au</div>
</section>

<section class="page page--back">
  <div class="page__photo" role="img" aria-label="Photograph placeholder: looking up between glass skyscrapers against a pale sky"></div>
  <svg class="page__waves" viewBox="0 0 520 735" aria-hidden="true">
    <defs>
      <linearGradient id="backDark" x1="0" y1="0" x2="0" y2="1">
        <stop offset="0" stop-color="#2b2e35" stop-opacity="0.95"/>
        <stop offset="1" stop-color="#0b0e14"/>
      </linearGradient>
    </defs>
    <path d="M0 395 C90 430 190 480 270 470 C350 460 400 330 440 270 C470 230 500 215 520 210 L520 735 L0 735 Z" fill="url(#backDark)"/>
    <path d="M0 385 C100 390 200 430 260 440" fill="none" stroke="var(--brand-blue)" stroke-width="1"/>
    <path d="M0 415 C90 440 190 480 270 470 C350 460 400 330 440 270 C470 230 500 215 520 210" fill="none" stroke="#fff" stroke-width="1.5"/>
    <rect x="0" y="698" width="520" height="37" fill="var(--night)"/>
  </svg>
  <div class="brand"><span class="brand__dot"></span><span class="brand__name">Marlowe<br>Consulting</span></div>
  <p class="back__lead">Contact us to find out how Marlowe Consulting can help build your company into a market leader today.</p>
  <div class="contacts">
    <div class="contact">
      <p class="contact__name">Julian Marlowe</p>
      <p>Managing Director</p>
      <p class="contact__row"><svg class="contact__icon" viewBox="0 0 12 12"><circle cx="6" cy="6" r="5.3" fill="none" stroke="#fff"/><path d="M4 3.5 L5 3.5 L5.4 5 L4.8 5.5 C5.2 6.4 5.7 6.9 6.5 7.2 L7 6.6 L8.5 7 L8.5 8 C6 8.3 3.7 6 4 3.5 Z" fill="#fff"/></svg>+61 400 555 018</p>
      <p class="contact__row"><svg class="contact__icon" viewBox="0 0 12 12"><circle cx="6" cy="6" r="5.3" fill="none" stroke="#fff"/><rect x="3.3" y="4.2" width="5.4" height="3.6" fill="#fff"/></svg>julian@marloweconsulting.com.au</p>
    </div>
    <div class="contact">
      <p class="contact__name">Oscar Marlowe</p>
      <p>Managing Director</p>
      <p class="contact__row"><svg class="contact__icon" viewBox="0 0 12 12"><circle cx="6" cy="6" r="5.3" fill="none" stroke="#fff"/><path d="M4 3.5 L5 3.5 L5.4 5 L4.8 5.5 C5.2 6.4 5.7 6.9 6.5 7.2 L7 6.6 L8.5 7 L8.5 8 C6 8.3 3.7 6 4 3.5 Z" fill="#fff"/></svg>+61 400 555 027</p>
      <p class="contact__row"><svg class="contact__icon" viewBox="0 0 12 12"><circle cx="6" cy="6" r="5.3" fill="none" stroke="#fff"/><rect x="3.3" y="4.2" width="5.4" height="3.6" fill="#fff"/></svg>oscar@marloweconsulting.com.au</p>
    </div>
  </div>
  <div class="band">
    <span>marloweconsulting.com.au</span>
    <span class="follow">Follow us <span class="follow__icon"></span><span class="follow__icon"></span></span>
  </div>
</section>

</body>
</html>
```